Upmarket, mysterious, eye-catching box design for oral care product.

Teeth are like crops in the fields; and gums play the same role as fields. If fields are not irrigated and fertilized properly, crops cannot be harvested. So, logistically, if gums are not healthy, we cannot have healthy teeth. Our product are bottles of herbal nutrition to feed our customers’ gums. Every drop of our product is previous for oral care, especially for the health of gums. I wish you guys could source out characteristics of our product and build them up by designs.

Before you start your job, pls remember my analogy and let your designs fly in imagination.

Target Market(s)

female from 18 to 50

Industry/Entity Type

oral care

Requirements
Must have
• good taste
Nice to have
• imagination

```html
<!DOCTYPE html>
<html lang="en">
<head>
<meta charset="utf-8">
<title>verdolune Aligner gel – box panels</title>
<link rel="stylesheet" href="https://fonts.googleapis.com/css2?family=Montserrat:wght@500;600;700;800&display=swap">
<style>
  :root {
    --bg: #ffffff;
    --white: #ffffff;
    --green-light: #4f9a3c;
    --green-mid: #2f7a2a;
    --green-dark: #1d5a1c;
    --green-deep: #154a16;
    --ink-dark: #2f4a2a;
    --leaf: #5fbf45;
    --tooth: #eef1ee;
  }
  * { margin: 0; padding: 0; box-sizing: border-box; }
  html, body { width: 1200px; height: 917px; overflow: hidden; background: var(--bg); }
  body { font-family: "Montserrat", Arial, sans-serif; }
  .canvas { position: relative; width: 1200px; height: 917px; }

  .panel { position: absolute; top: 100px; height: 700px; overflow: hidden; }
  .panel__top { position: absolute; left: 0; top: 0; width: 100%; height: 100%; }

  /* Side panel */
  .side { left: 330px; width: 150px; background: linear-gradient(180deg, var(--green-mid) 0%, var(--green-dark) 100%); }
  .side__cap { position: absolute; left: 0; top: 0; width: 150px; height: 150px; }
  .side__tagline { position: absolute; left: 14px; top: 22px; width: 126px; font-size: 12px; font-weight: 600; line-height: 1.35; color: var(--ink-dark); }
  .benefits { position: absolute; left: 12px; top: 235px; list-style: none; }
  .benefit { display: flex; align-items: center; gap: 8px; margin-bottom: 42px; }
  .benefit__icon { width: 34px; height: 34px; border-radius: 50%; border: 1.5px solid rgba(255,255,255,.8); flex: none; }
  .benefit__text { font-size: 9px; font-weight: 700; line-height: 1.3; color: var(--white); text-transform: uppercase; }
  .side__botanical { position: absolute; left: 0; bottom: 0; width: 150px; height: 260px;
    background: radial-gradient(ellipse at 30% 70%, rgba(255,255,255,.12), rgba(255,255,255,0) 70%); }

  /* Front panel */
  .front { left: 480px; width: 390px; background: linear-gradient(180deg, var(--green-light) 0%, var(--green-mid) 45%, var(--green-deep) 100%); }
  .brand { position: absolute; left: 0; top: 58px; width: 100%; display: flex; justify-content: center; align-items: center; gap: 8px; }
  .brand__name { font-size: 36px; font-weight: 800; color: var(--green-mid); letter-spacing: -0.5px; }
  .brand__dot { width: 14px; height: 14px; border-radius: 50%; background: var(--green-mid); }

  .product { position: absolute; left: 48px; top: 240px; color: var(--white); }
  .product__name { font-size: 66px; font-weight: 800; line-height: 1; letter-spacing: -1px; }
  .product__row { display: flex; align-items: flex-start; gap: 10px; margin-top: -2px; }
  .product__type { font-size: 66px; font-weight: 800; line-height: .9; letter-spacing: -1px; }
  .product__desc { font-size: 17px; font-weight: 700; line-height: 1.2; padding-top: 8px; }

  .hero { position: absolute; left: 95px; top: 420px; width: 210px; height: 200px; border-radius: 50%;
    background: radial-gradient(ellipse at 50% 55%, var(--tooth) 0%, var(--tooth) 22%, var(--leaf) 40%, var(--green-dark) 72%, rgba(21,74,22,0) 100%); }

  .volume { position: absolute; left: 0; bottom: 52px; width: 100%; text-align: center; font-size: 17px; font-weight: 600; color: var(--white); }
</style>
</head>
<body>
<main class="canvas">

  <section class="panel side">
    <svg class="side__cap" viewBox="0 0 150 150" aria-hidden="true">
      <path d="M0 0 H150 V95 C110 125 55 140 0 150 Z" fill="var(--white)"/>
    </svg>
    <p class="side__tagline">Immune Support for Oral Health</p>
    <ul class="benefits">
      <li class="benefit"><span class="benefit__icon" role="img" aria-label="Tooth with aligner icon"></span><span class="benefit__text">- Reduce pain<br>from aligners</span></li>
      <li class="benefit"><span class="benefit__icon" role="img" aria-label="Sparkling tooth icon"></span><span class="benefit__text">- Maintain<br>dental hygiene</span></li>
      <li class="benefit"><span class="benefit__icon" role="img" aria-label="Strong tooth icon"></span><span class="benefit__text">- Strengthen<br>gums</span></li>
    </ul>
    <div class="side__botanical" role="img" aria-label="Faint botanical line drawing"></div>
  </section>

  <section class="panel front">
    <svg class="panel__top" viewBox="0 0 390 700" preserveAspectRatio="none" aria-hidden="true">
      <path d="M0 0 H390 V150 C300 130 190 175 110 200 C60 214 25 210 0 200 Z" fill="var(--white)"/>
    </svg>
    <div class="brand">
      <span class="brand__name">verdolune</span>
      <span class="brand__dot"></span>
    </div>
    <div class="product">
      <h1 class="product__name">Aligner</h1>
      <div class="product__row">
        <span class="product__type">gel</span>
        <span class="product__desc">Herbal Extracts<br>and Formulas</span>
      </div>
    </div>
    <div class="hero" role="img" aria-label="White tooth resting on fresh green mint leaves"></div>
    <p class="volume">30ml E</p>
  </section>

</main>
</body>
</html>
```